Norwegian psychologist service needs a fresh and exiting web site*

Norwegian psychologist service: working with therapy, personal development, mastery and personal growth. Focus: children and teenagers with special needs; family dynamics; group processes; individuals with a need for therapy and personal growth. (Our company name: Fjordlys og samhold (means Mastery and Growth).

We already have a logo for the company, which will be used (will be attached in the project).

The webside is to be structured in 4 pages with roll down curtain menus (the numbers are just for guiding the designer - the should not be added):

Page 1: Om Fjordlys og Samhold (about Mastery and Growth): this is where our business is is presented/described shortly: Lorem Ipsum dolor cit...

Page 2: Tjenester (Services): this is where our 5 service areas are presented:
2.1 Utredning (Investigation, diagnosing): Lorem Ipsum dolor cit...
2.2 Rådgivning (consulting): Lorem Ipsum dolor cit...

2.3 Kurs og work shops (courses and work shops): Lorem Ipsum dolor cit...
2.3a Fjordlys og samhold Tema 1 (T1)
2.3b Fjordlys og samhold Tema 2 (T2)
2.3c Fjordlys og samhold Tema 3 (T3)

2.4 Terapi og utvikling (Therapy and development)
2.4a Fjordlys og samhold for individer (FS1)
2.4b Fjordlys og samhold i familier (FS2)
2.4c Fjordlys og samhold i grupper (FS3)
2.4d Fjordlys og samhold i institusjoner (FS4)

Page 3: Aktuelt (Blog): this is our blog where we share knowledge and articles

Page 4: Kontakt (Contact): This is the contact form page. Contact form should constitute:
- Ditt navn (your name)
- E-post (your e-mail)
- Emne (subject)
- Melding (message/description)

Our project should also include suggestion for handheld units (iPhone, iPad).
Updates

We have both been traveling with work for a while, and then unfortunately both of us got sick on return, so we need a few more days to evaluate and choose design. Kind Regards Arvid & Margit

Target Market(s)

Focus on therapy, learning, mastery and growth for children and teenagers with special needs, within the family dynamics, or in a group setting.
OUR MARKETS:
Private market: individuals, families, groups and health industry institutions (with focus on learning, mastery, growth (as well as growing up) and psychiatry for children and teenagers with special difficulties and needs)
Public institutions: Government institutions, state institutions and municipality institutions (e.g. schools, municipality health service, hospitals) that serve the public (families with children and teenagers with special needs, and where learning, mastery, growth (as well as growing up) and potential psychiatry is an issue).

Number of Pages Required

4 page

Font styles to use
Sans Serif

Colors

Designer to choose colors to be used in the design.

Requirements
Must have
• The website must have 4 pages with roll down curtain menus (we have added a PDF with suggested structure, and headings, with sub menus - see attached PDF drawing.
• The web page must also use the added logo file - and make the web page work well with our logo.
• We would like the website to have a modern look and we would like the site to be associated with typical HIGH END TOP QUALITY private health institutions, but with a stronger focus on human beings (hands, faces etc), and not white coats and doctors. We are psychologists in the private market.
• For instance, if photos are being used - we tend to like "warm" almost art-like, "grainy" two-tone (e.g. sepia) photos to illustrate our focus. If designer can find such photos as part of design, it would be interesting to us. We would like a few photos like that integrated in the design.
• We also want a design suggestion for how the web page should look like and behave on handheld units (e.g. iPhone, iPad).
Nice to have
• If designer could find a number of suitable photos that matches the business idea and design requirements (see description above), that could follow website, that would be good.
• It could also be nice to have graphic symbols that denote the different pages/subpages (subjects)....
• HORSES: we sometimes use horses as a "tool" in therapy sessions. The horse is not necessarily used for riding, but for contact, communication and grooming. PHOTOS: we would like the designer to find an opportunity for using a photo reflecting this cooperation between therapist, child, teenager and horse. It is a bit up to the designer to find a way to do this... Since the horse is only a tool, among many other tools, it does not have to be much - but we want to try and see how it will work with a photo that also reflects this part of our business.

```html
<!DOCTYPE html>
<html lang="en">
<head>
<meta charset="utf-8">
<title>Fjordlys og samhold</title>
<link rel="stylesheet" href="https://fonts.googleapis.com/css2?family=Damion&family=Hind:wght@400;500;600&family=Poppins:wght@400;500;600&display=swap">
<style>
:root{
  --green:#0c5e2e;
  --green-light:#5aa84a;
  --blue:#2c3a8e;
  --blue-soft:#4b56a8;
  --text:#2a2a2a;
  --muted:#555;
  --tint:#f1f6f4;
  --dark:#232325;
  --darker:#1b1b1c;
  --white:#fff;
}
*{margin:0;padding:0;box-sizing:border-box}
html,body{width:1200px;height:2281px;overflow:hidden;background:var(--white)}
body{position:relative;font-family:"Poppins",sans-serif;color:var(--text)}
.abs{position:absolute}
.script{font-family:"Damion",cursive;font-weight:400}
.heading{font-family:"Hind",sans-serif;font-weight:500}

/* header */
.brand{left:131px;top:22px;display:flex;align-items:center;gap:8px;font-family:"Hind",sans-serif;font-weight:500;font-size:19px;color:var(--blue)}
.brand .dot{width:26px;height:26px;border-radius:50%;background:var(--blue)}
.nav{left:355px;top:34px;display:flex;font-size:8.5px;font-weight:600;letter-spacing:.1px}
.nav a{color:#222;text-decoration:none;position:absolute;white-space:nowrap}
.nav a.active{color:var(--blue)}
.btn{display:flex;align-items:center;justify-content:center;color:var(--white);font-size:8.5px;font-weight:600;border-radius:2px}
.btn-green{background:var(--green)}
.btn-blue{background:var(--blue)}
.call{left:940px;top:26px;font-size:18px;color:var(--blue)}
.call b{font-weight:600}

/* hero */
.hero{left:0;top:78px;width:1200px;height:470px}
.hero-arrow{width:44px;height:43px;background:rgba(255,255,255,.85);top:251px;color:#999;font-size:12px;display:flex;align-items:center;justify-content:center}
.hero-kicker{left:235px;top:190px;color:var(--white);font-size:24px}
.hero-title{left:234px;top:224px;color:var(--white);font-family:"Hind",sans-serif;font-weight:500;font-size:41px;line-height:45px;letter-spacing:.3px}

/* about */
.about-art{left:270px;top:589px;width:297px;height:341px}
.kicker{color:var(--green);font-size:24px}
.about-text{left:591px;top:600px;width:375px}
.about-text h2{font-size:21px;color:#222;margin-top:-2px}
.about-text .lead{font-size:12.6px;line-height:19px;margin-top:11px;color:#222}
.about-text .body{font-size:10.4px;line-height:18.7px;margin-top:14px;color:#333}

/* services */
.services-bg{left:0;top:995px;width:1200px;height:510px}
.services-head{left:0;top:1045px;width:1200px;text-align:center;color:var(--white)}
.services-head .kicker{color:var(--white)}
.services-head h2{font-size:21px;margin-top:-2px}
.services-head p{font-size:12.4px;font-weight:600;line-height:19px;margin-top:12px}
.card{top:1193px;width:170px;height:178px;background:var(--white);border-radius:3px;text-align:center;padding-top:17px}
.card .icon{width:52px;height:52px;border-radius:50%;background:#eef0f2;margin:0 auto;display:flex;align-items:center;justify-content:center}
.card h3{font-family:"Hind",sans-serif;font-weight:500;font-size:14px;line-height:19px;margin-top:8px;color:#222}
.card p{font-size:8.4px;line-height:15px;color:#444;margin-top:6px;padding:0 10px}

/* testimonials */
.testi-head{left:0;top:1536px;width:1200px;text-align:center}
.testi-head h2{font-size:21px;color:#222;margin-top:-2px}
.quote{top:1640px;width:356px;height:136px;background:var(--tint)}
.quote .mark{position:absolute;left:18px;top:24px;font-family:"Damion",cursive;font-size:34px;color:var(--green);line-height:1}
.quote p{position:absolute;left:47px;top:30px;width:290px;font-size:13px;line-height:18.7px;color:#333}
.quote::after{content:"";position:absolute;left:30px;bottom:-10px;border-left:10px solid transparent;border-right:10px solid transparent;border-top:10px solid var(--tint)}
.author{top:1799px}
.author b{display:block;font-size:9.5px;font-weight:600;color:var(--blue)}
.author span{display:block;font-size:10px;color:#666;margin-top:3px}
.dots{left:567px;top:1880px;display:flex;gap:6px}
.dots i{width:5px;height:5px;border-radius:50%;background:#c5cae4}
.dots i:first-child{background:var(--blue)}

/* footer */
.footer-base{left:0;top:1940px;width:1200px;height:341px}
.f-brand{left:235px;top:2068px;font-family:"Hind",sans-serif;font-weight:500;font-size:17px;color:var(--blue);display:flex;align-items:center;gap:7px}
.f-brand .dot{width:20px;height:20px;border-radius:50%;background:var(--blue)}
.f-about{left:235px;top:2107px;width:205px;font-size:8.6px;line-height:16px;color:var(--white)}
.social{top:2167px;width:26px;height:26px;border:1px solid var(--white);border-radius:50%}
.f-title{top:2046px;font-family:"Hind",sans-serif;font-weight:500;font-size:11.5px;color:var(--white);letter-spacing:.2px}
.f-links{left:476px;top:2080px;list-style:none}
.f-links li{font-size:8.6px;color:var(--white);height:22.5px}
.f-links li::before{content:"›";margin-right:10px}
.contact-row{left:594px;display:flex;align-items:center;gap:11px;color:var(--white);font-size:8.6px;line-height:15px}
.contact-row .ic{width:20px;height:20px;border-radius:50%;background:var(--green);display:flex;align-items:center;justify-content:center;flex:none}
.news-text{left:797px;top:2080px;width:170px;font-size:8.6px;line-height:15px;color:var(--white)}
.news-input{left:797px;top:2123px;width:169px;height:24px;background:var(--white);border-radius:12px;font-size:8.4px;color:#777;display:flex;align-items:center;padding-left:25px}
.news-send{left:928px;top:2123px;width:38px;height:24px;border-radius:0 12px 12px 0;background:var(--green);display:flex;align-items:center;justify-content:center}
.copyright{left:0;top:2239px;width:1200px;height:42px;background:var(--darker);font-size:8.8px;color:var(--white);text-align:center;line-height:42px}
.copyright em{font-style:normal;color:var(--green-light)}
</style>
</head>
<body>

<header>
  <div class="abs brand"><span class="dot"></span>Fjordlys og samhold</div>
  <nav class="abs nav">
    <a class="active" style="left:0">HOME</a>
    <a style="left:51px">ABOUT FJORDLYS OG SAMHOLD</a>
    <a style="left:211px">SERVICES</a>
    <a style="left:278px">BLOG</a>
    <a style="left:326px">CONTACT</a>
  </nav>
  <div class="abs btn btn-green" style="left:763px;top:20px;width:153px;height:35px">MAKE AN APPOINTMENT</div>
  <div class="abs call">Call: <b>555 210 7788</b></div>
</header>

<section>
  <svg class="abs hero" viewBox="0 0 1200 470" role="img" aria-label="Photo of a child playing with blocks and a therapist holding a clipboard, tinted green">
    <defs>
      <linearGradient id="heroFill" x1="0" y1="0" x2="1" y2="0">
        <stop offset="0" stop-color="#86b29d"/>
        <stop offset=".5" stop-color="#78a892"/>
        <stop offset="1" stop-color="#6e9f88"/>
      </linearGradient>
      <linearGradient id="edge" x1="0" y1="0" x2="1" y2="0">
        <stop offset="0" stop-color="#2c3a8e"/>
        <stop offset=".5" stop-color="#3f6a6a"/>
        <stop offset="1" stop-color="#5aa84a"/>
      </linearGradient>
    </defs>
    <path d="M0 0H1200V369Q600 522 0 369Z" fill="url(#edge)"/>
    <path d="M0 0H1200V369Q600 505 0 369Z" fill="url(#heroFill)"/>
  </svg>
  <div class="abs hero-arrow" style="left:0">‹</div>
  <div class="abs hero-arrow" style="left:1156px">›</div>
  <div class="abs script hero-kicker">I could help you to</div>
  <h1 class="abs hero-title">PSYCHOLOGICAL CARE<br>AT THE HIGHEST LEVEL</h1>
  <div class="abs btn btn-green" style="left:234px;top:335px;width:153px;height:34px">MAKE AN APPOINTMENT</div>
  <div class="abs btn btn-blue" style="left:397px;top:335px;width:76px;height:34px">ABOUT US</div>
  <svg class="abs" style="left:585px;top:518px" width="30" height="18" viewBox="0 0 30 18">
    <path d="M0 18A15 15 0 0 1 30 18Z" fill="#fff"/>
    <path d="M12 10l3 3 3-3" fill="none" stroke="#aaa" stroke-width="1"/>
  </svg>
</section>

<section>
  <svg class="abs about-art" viewBox="0 0 297 341" role="img" aria-label="Tree-shaped illustration filled with photos of hands and a smiling child">
    <defs>
      <linearGradient id="artFill" x1="0" y1="0" x2="0" y2="1">
        <stop offset="0" stop-color="#8c8fc6"/>
        <stop offset=".55" stop-color="#7aa98f"/>
        <stop offset="1" stop-color="#b58e97"/>
      </linearGradient>
    </defs>
    <rect width="297" height="341" rx="6" fill="url(#artFill)" opacity=".75"/>
  </svg>
  <div class="abs about-text">
    <div class="script kicker">about us</div>
    <h2 class="heading">We Are The Best Support for You</h2>
    <p class="lead">Lorem ipsum dolor sit amet, consectetur adipiscing elit. Aenean sit amet pretium nisi. Aenean turpis neque, lutpat at felis eu, iaculis imperdiet neque.</p>
    <p class="body">Ut accumsan felis purus. Donec consequat condimentum bibendum. Phasellus ultricies molestie eros id volutpat. Nullam a lacinia nisl. Aliquam vestibulum massa ut dolor tincidunt, ac vulputate magna dignissim. Integer nec leo nec sem luctus rhoncus. Phasellus blandit iaculis enim, sit amet bibendum odio semper vitae.</p>
    <p class="body" style="margin-top:18px">In quis nunc odio. Praesent sit amet velit velit. Morbi ornare risus quis magna pharetra, vel pulvinar risus rhoncus. Pellentesque diam metus, tincidunt sed tincidunt at, interdum eget quam. Aliquam ornare varius quam sit amet luctus. Vivamus facilisis vehicula sapien quis ultricies.</p>
  </div>
</section>

<section>
  <svg class="abs services-bg" viewBox="0 0 1200 510" role="img" aria-label="Photo of hands filling in a patient form, tinted blue">
    <defs>
      <linearGradient id="svcFill" x1="0" y1="0" x2="1" y2="1">
        <stop offset="0" stop-color="#5b5da6"/>
        <stop offset=".5" stop-color="#4a57ad"/>
        <stop offset="1" stop-color="#4d5fb4"/>
      </linearGradient>
    </defs>
    <path d="M0 0H1200V411Q600 565 0 411Z" fill="url(#edge)"/>
    <path d="M0 0H1200V411Q600 548 0 411Z" fill="url(#svcFill)"/>
  </svg>
  <div class="abs services-head">
    <div class="script kicker">my services</div>
    <h2 class="heading">What Service Provide</h2>
    <p>Lorem ipsum dolor sit amet, consectetur adipiscing elit.<br>Aenean sit amet pretium nisi.</p>
  </div>
  <div class="abs card" style="left:233px">
    <div class="icon"><svg width="26" height="26" viewBox="0 0 26 26" fill="none" stroke="#444" stroke-width="1.2"><circle cx="11" cy="11" r="7"/><path d="M16 16l7 7"/><circle cx="11" cy="11" r="3" fill="#f0a030" stroke="none"/></svg></div>
    <h3>Investigation,<br>Diagnosing</h3>
    <p>Lorem ipsum dolor sit amet, consectetur adipiscing elit. Aenean sit amet pretium nisi.</p>
  </div>
  <div class="abs card" style="left:421px">
    <div class="icon"><svg width="26" height="26" viewBox="0 0 26 26" fill="none" stroke="#2c3a8e" stroke-width="1.4"><circle cx="13" cy="13" r="10"/><circle cx="13" cy="13" r="6"/><circle cx="13" cy="13" r="2" fill="#2c3a8e"/></svg></div>
    <h3>Consulting</h3>
    <p>Lorem ipsum dolor sit amet, consectetur adipiscing elit. Aenean sit amet pretium nisi.</p>
  </div>
  <div class="abs card" style="left:609px">
    <div class="icon"><svg width="26" height="26" viewBox="0 0 26 26" fill="none" stroke="#444" stroke-width="1.2"><path d="M6 22v-5a8 8 0 1 1 13-6l2 5h-3v3h-4v3"/><circle cx="13" cy="10" r="4" fill="#3bb3a8" stroke="none"/></svg></div>
    <h3>Courses and<br>Work Shops</h3>
    <p>Lorem ipsum dolor sit amet, consectetur adipiscing elit. Aenean sit amet pretium nisi.</p>
  </div>
  <div class="abs card" style="left:796px">
    <div class="icon"><svg width="26" height="26" viewBox="0 0 26 26" fill="none" stroke="#444" stroke-width="1.2"><path d="M13 24V12M13 16l-5-4M13 14l5-5M13 12V5"/><circle cx="13" cy="11" r="9"/></svg></div>
    <h3>Therapy and<br>Development</h3>
    <p>Lorem ipsum dolor sit amet, consectetur adipiscing elit. Aenean sit amet pretium nisi.</p>
  </div>
</section>

<section>
  <div class="abs testi-head">
    <div class="script kicker">testimonials</div>
    <h2 class="heading">Happy Clients About Me</h2>
  </div>
  <div class="abs quote" style="left:235px">
    <span class="mark">“</span>
    <p>Lorem ipsum dolor sit amet, consectetur adipiscing elit. Aenean sit amet pretium nisi. Aenean turpis neque, volutpat at felis eu, iaculis imperdiet neque.</p>
  </div>
  <div class="abs quote" style="left:609px">
    <span class="mark">“</span>
    <p>Lorem ipsum dolor sit amet, consectetur adipiscing elit. Aenean sit amet pretium nisi. Aenean turpis neque, volutpat at felis eu, iaculis imperdiet neque.</p>
  </div>
  <div class="abs author" style="left:264px"><b>INGRID DAHL</b><span>25 years</span></div>
  <div class="abs author" style="left:639px"><b>INGRID DAHL</b><span>25 years</span></div>
  <div class="abs dots"><i></i><i></i><i></i><i></i><i></i><i></i></div>
</section>

<footer>
  <svg class="abs footer-base" viewBox="0 0 1200 341">
    <path d="M0 104Q600 -40 1200 104V341H0Z" fill="url(#edge)"/>
    <path d="M0 104Q600 -25 1200 104V341H0Z" fill="var(--dark)"/>
  </svg>
  <div class="abs f-brand"><span class="dot"></span>Fjordlys og samhold</div>
  <p class="abs f-about">Lorem ipsum dolor sit amet, consectetur adipiscing elit. Etiam efficitur dolor massa, ac molestie sem lacinia vel.</p>
  <span class="abs social" style="left:234px" aria-label="Social profile"></span>
  <span class="abs social" style="left:266px" aria-label="Social profile"></span>
  <span class="abs social" style="left:298px" aria-label="Social profile"></span>

  <div class="abs f-title" style="left:471px">QUICK LINKS</div>
  <ul class="abs f-links">
    <li>Home</li><li>About Us</li><li>Services</li><li>Blog</li><li>Contact Us</li>
  </ul>

  <div class="abs f-title" style="left:595px">GET IN TOUCH</div>
  <div class="abs contact-row" style="top:2078px"><span class="ic"><svg width="10" height="10" viewBox="0 0 10 10"><path d="M2 1l2 2-1 1.5a6 6 0 0 0 2.5 2.5L7 6l2 2-1.5 1.5C4 9 1 6 .5 2.5Z" fill="#fff"/></svg></span>+ 47 400 12 345</div>
  <div class="abs contact-row" style="top:2110px"><span class="ic"><svg width="10" height="8" viewBox="0 0 10 8"><rect width="10" height="8" rx="1" fill="#fff"/><path d="M0 1l5 3.5L10 1" fill="none" stroke="#0c5e2e"/></svg></span>post@fjordlys.example</div>
  <div class="abs contact-row" style="top:2145px"><span class="ic"><svg width="8" height="11" viewBox="0 0 8 11"><path d="M4 11S0 6.5 0 4a4 4 0 0 1 8 0c0 2.5-4 7-4 7Z" fill="#fff"/><circle cx="4" cy="4" r="1.5" fill="#0c5e2e"/></svg></span>45 Strandgata, Sentrum,<br>Bergen, 5013</div>

  <div class="abs f-title" style="left:797px">NEWSLETTER</div>
  <p class="abs news-text">Enter your email to receive updates and specials</p>
  <div class="abs news-input">Email Address</div>
  <div class="abs news-send"><svg width="13" height="12" viewBox="0 0 13 12"><path d="M0 5L13 0 9 12 6 7Z" fill="#fff"/></svg></div>

  <div class="abs copyright">Copyright © 2020 <em>Fjordlys og samhold</em>. All Rights Reserved</div>
</footer>

</body>
</html>
```